Super urgent - business card design

I need to design a business card
on the front side the words "VORTAL CAPITAL" with the top half surrounded by a stylised cloud. Minimalist, navy blue font on white background, with the Vortal capital in embossing.

On the back contact details (avoid centered). I would rather have the details taking the 2/3rd on the right and having the logo on the left, but anyway not plain centered

Renato Lo Cascio
CEO e Fondatore

r.locascio@vortal-capital.example
+39.347.512.6084

Piazza Torcelli 7
20135 Milano

```html
<!DOCTYPE html>
<html lang="it">
<head>
<meta charset="utf-8">
<title>Vortal Capital – Business Card</title>
<link rel="stylesheet" href="https://fonts.googleapis.com/css2?family=Cinzel:wght@500;600&family=Montserrat:wght@300;400&display=swap">
<style>
  :root {
    --backdrop: #dedede;
    --card: #f5f5f5;
    --navy: #1b2540;
    --ink: #33363d;
  }
  * { margin: 0; padding: 0; box-sizing: border-box; }
  html, body {
    width: 1200px; height: 1124px; overflow: hidden;
    background: var(--backdrop);
  }
  .sheet { position: relative; width: 1200px; height: 1124px; }
  .card {
    position: absolute; left: 252px; width: 696px; height: 398px;
    background: var(--card); border-radius: 24px;
  }
  .card--contact { top: 134px; }
  .card--brand { top: 592px; }

  .wordmark { position: absolute; text-align: center; color: var(--navy);
    font-family: "Cinzel", serif; font-weight: 600; line-height: 1; }
  .wordmark__name { display: block; }
  .wordmark__sub { display: block; }

  .card--contact .wordmark { right: 44px; top: 96px; width: 200px; }
  .card--contact .wordmark__name { font-size: 30px; letter-spacing: 9px; margin-right: -9px; }
  .card--contact .wordmark__sub { font-size: 15px; letter-spacing: 5px; margin-right: -5px; margin-top: 4px; }

  .card--brand .wordmark { left: 0; right: 0; top: 196px; }
  .card--brand .wordmark__name { font-size: 54px; letter-spacing: 20px; margin-right: -20px; }
  .card--brand .wordmark__sub { font-size: 27px; letter-spacing: 10px; margin-right: -10px; margin-top: 8px; }

  .person { position: absolute; left: 42px; top: 213px; }
  .person__name { font-family: "Cinzel", serif; font-weight: 600; font-size: 23px;
    color: var(--navy); line-height: 1; letter-spacing: 0.3px; }
  .person__role { font-family: "Montserrat", sans-serif; font-weight: 400; font-size: 15px;
    color: var(--ink); margin-top: 5px; }

  .divider { position: absolute; left: 41px; right: 41px; top: 283px;
    height: 1px; background: var(--navy); }

  .contact, .address { position: absolute; top: 310px;
    font-family: "Montserrat", sans-serif; font-weight: 400; font-size: 15.5px;
    color: var(--ink); line-height: 25px; }
  .contact { left: 41px; }
  .contact__row { display: flex; align-items: center; gap: 5px; }
  .contact__icon { width: 11px; height: 11px; fill: var(--navy); }
  .address { right: 41px; text-align: right; }
</style>
</head>
<body>
<main class="sheet">
  <section class="card card--contact">
    <div class="wordmark">
      <span class="wordmark__name">VORTAL</span>
      <span class="wordmark__sub">CAPITAL</span>
    </div>
    <div class="person">
      <p class="person__name">RENATO LO CASCIO</p>
      <p class="person__role">CEO e Fondatore</p>
    </div>
    <div class="divider"></div>
    <div class="contact">
      <p class="contact__row">
        <svg class="contact__icon" viewBox="0 0 24 24" aria-hidden="true"><path d="M6.6 10.8a15.1 15.1 0 0 0 6.6 6.6l2.2-2.2c.3-.3.7-.4 1-.2 1.1.4 2.3.6 3.6.6.6 0 1 .4 1 1V20c0 .6-.4 1-1 1C10.6 21 3 13.4 3 4c0-.6.4-1 1-1h3.5c.6 0 1 .4 1 1 0 1.3.2 2.5.6 3.6.1.3 0 .7-.2 1z"/></svg>
        +39.347.512.6084
      </p>
      <p class="contact__row">
        <svg class="contact__icon" viewBox="0 0 24 24" aria-hidden="true"><path d="M2 9l10-7 10 7v12H2zM4 10.2V19h16v-8.8l-8 5.3z"/></svg>
        r.locascio@vortal-capital.example
      </p>
    </div>
    <div class="address">
      <p>Piazza Torcelli 7</p>
      <p>20135 Milano</p>
    </div>
  </section>

  <section class="card card--brand">
    <div class="wordmark">
      <span class="wordmark__name">VORTAL</span>
      <span class="wordmark__sub">CAPITAL</span>
    </div>
  </section>
</main>
</body>
</html>
```